Quillby Housecrafters Door Hanger design, Postcard and presentation folders Design

we are a home improvement company in Portland Oregon, are main service is roofing but we also do gutters, painting and pressure washing. we are a certified roofing contractor for TRV. We have over 20years of experince in the roofing industry we use top quality materials. Our mission is to do quality work and provide the best service.
Updates

This door hangers are going to be share to homeowners where we are currently working at! I will like to have a square maybe 2 inch wide and 1 inch hide (blank) for me to put the address where we are working at. So we want to give a direct message to homeowners who we are and why we are there for. Our services are roofing, gutters, painting, and pressure washing. But 95% of the door hangers should give the message that we are a roofing contractor. We are also certified by TRV which means all of our new roof projects have a 50 year warranty which only 2% of roofing contractor can offer that. We also offer finance, and all quality work. I will like to add photos of our trucks since all of them are wrap which will build them trust.

Target Market(s)

This door hangers should be custom for Homeowners with residential Homes,,, Average customer are between 40 & 65 Years old.

Industry/Entity Type

Roofing

Contact Information for Business Card

Logo, name, phone number, credentials, and services like roofing gutters painting and pressure washing

Font styles to use
Serif
Sans Serif
Decorative

Colors
33b8a4
5c5c5c

Requirements
Must have
• I want tho have a folder design just like this business card sample i uploaded. Teal and charcoal with services ...
Nice to have
• company trucks, job photo, crew photo and credential photos
Should not have
• I dont want it too busy or crowded..

```html
<!DOCTYPE html>
<html lang="en">
<head>
<meta charset="utf-8">
<title>Quillby Housecrafters – Door Hanger</title>
<link href="https://fonts.googleapis.com/css2?family=Montserrat:wght@300;400;500;600;700;800;900&display=swap" rel="stylesheet">
<style>
  :root{
    --page:#e9e9ea;
    --teal:#1b9382;
    --teal-bright:#33b8a4;
    --charcoal:#2e2d30;
    --grey:#5c5c5c;
    --ink:#555;
    --white:#fff;
  }
  *{box-sizing:border-box;margin:0;padding:0}
  html,body{width:1200px;height:1200px;overflow:hidden}
  body{background:var(--page);font-family:"Montserrat",sans-serif;position:relative}
  .hanger{position:absolute;top:78px;width:430px;height:1044px;overflow:hidden;background:var(--charcoal);color:var(--white)}
  .hanger--front{left:168px}
  .hanger--back{left:602px}
  .hanger svg.shapes{position:absolute;inset:0}
  .abs{position:absolute}
  .center{left:0;width:100%;text-align:center}

  .corner-flag{width:170px;text-align:center;transform:rotate(45deg);transform-origin:center;font-weight:800;line-height:1;color:var(--white)}
  .corner-flag .big{font-size:26px;display:block}
  .corner-flag .small{font-size:15px;display:block;margin-top:2px}
  .corner-flag--split{display:flex;align-items:center;justify-content:center;gap:6px}
  .corner-flag--split .big{font-size:38px}
  .corner-flag--split .stack{font-size:12px;text-align:left;line-height:1.05}

  .warranty{left:34px;top:144px;width:98px;height:118px;background:var(--white);border-radius:6px 6px 6px 22px;text-align:center;color:var(--teal);font-weight:900;line-height:1;padding-top:6px}
  .warranty .num{font-size:50px;display:block;letter-spacing:-1px}
  .warranty .yrs{font-size:20px;display:block}
  .warranty .roof{font-size:21px;display:block;background:var(--teal);color:var(--white);margin:2px 0;padding:1px 0}
  .warranty .note{font-size:12px;display:block}

  .brand{font-family:"Montserrat",sans-serif;font-weight:800;color:var(--teal);line-height:1}
  .brand-mark{display:inline-block;width:18px;height:18px;background:var(--teal);margin-right:10px;vertical-align:middle}
  .tagline{font-weight:500;font-size:11px;letter-spacing:2px;color:#8a8a8a;text-transform:uppercase}

  .headline{font-weight:800;line-height:1;text-transform:uppercase}
  .teal{color:var(--teal)}
  .phone{font-weight:800;font-size:46px;color:var(--teal);letter-spacing:-0.5px}

  .touch{font-weight:800;font-size:14px;line-height:1.05;text-align:center}
  .touch .sub{color:var(--teal-bright);font-size:12px}

  .contact{left:30px;top:944px;font-size:12.5px;line-height:1}
  .contact li{list-style:none;display:flex;align-items:center;gap:7px;height:19px}
  .contact svg{flex:none}
  .contact strong{font-weight:700}
  .social{right:36px;top:944px;text-align:right;font-size:11px;font-weight:700}
  .social .dots{display:flex;gap:4px;justify-content:flex-end;margin:6px 0 8px}
  .social .dots span{width:20px;height:20px;border:1.5px solid var(--white);border-radius:50%}
  .license{font-weight:400;font-size:10.5px;line-height:1.25}

  .section-title{font-weight:800;font-size:25px;color:var(--teal)}
  .tile-label{font-size:10.5px;font-weight:600;text-transform:uppercase;background:var(--charcoal);padding:4px 14px 3px 6px;line-height:1}

  .quote{left:40px;top:684px;width:350px;font-size:12.6px;font-weight:400;line-height:15.5px;text-align:center}
  .quote-mark{font-weight:800;font-size:40px;line-height:1;color:var(--teal)}
  .quote-name{top:764px;font-weight:700;font-size:13px;color:var(--teal)}
  .quote-name span{background:var(--charcoal);padding:0 8px}

  .notice-head{left:53px;top:890px;width:325px;text-align:center;font-weight:800;font-size:15px;line-height:16px;color:var(--white)}
  .notice-list{left:69px;top:930px;width:293px;list-style:none}
  .notice-list li{display:flex;align-items:flex-end;height:22px;font-size:12px;color:var(--ink);text-transform:uppercase}
  .notice-list .lead{flex:1;border-bottom:1.5px dotted #888;margin:0 2px 3px}
  .notice-list .price{width:78px;border-bottom:1px solid #777;margin-bottom:3px}
</style>
</head>
<body>

<section class="hanger hanger--front">
  <svg class="shapes" width="430" height="1044" viewBox="0 0 430 1044">
    <defs>
      <linearGradient id="skyRoof" x1="0" y1="0" x2="0" y2="1">
        <stop offset="0" stop-color="#6f8a99"/>
        <stop offset="0.4" stop-color="#b7c6cf"/>
        <stop offset="0.62" stop-color="#5aa2c4"/>
        <stop offset="1" stop-color="#353a40"/>
      </linearGradient>
    </defs>
    <rect width="430" height="500" fill="url(#skyRoof)" role="img" aria-label="Photo of a roofing crew laying underlayment on a house roof under a cloudy sky"/>
    <polygon points="0,462 216,336 430,462 430,1044 0,1044" fill="var(--teal)"/>
    <polygon points="0,486 216,362 430,486 430,1044 0,1044" fill="var(--charcoal)"/>
    <path d="M44,572 V560 H386 V572" fill="none" stroke="var(--teal)" stroke-width="2"/>
    <rect x="0" y="638" width="430" height="104" fill="var(--grey)"/>
    <rect x="44" y="742" width="342" height="68" fill="var(--white)" stroke="var(--teal)" stroke-width="2"/>
    <polygon points="198,741 234,741 216,757" fill="var(--grey)"/>
    <polygon points="0,924 216,884 430,924 430,1044 0,1044" fill="var(--grey)"/>
    <polygon points="0,934 216,896 430,934 430,1044 0,1044" fill="var(--teal)"/>
    <polygon points="216,860 252,880 252,920 216,940 180,920 180,880" fill="var(--grey)"/>
    <polygon points="268,0 430,0 430,150" fill="var(--teal)"/>
    <polygon points="118,0 154,0 236,100 204,120" fill="var(--white)"/>
    <circle cx="226" cy="130" r="80" fill="var(--white)"/>
  </svg>

  <div class="abs corner-flag" style="left:290px;top:38px"><span class="big">FREE</span><span class="small">ESTIMATES!</span></div>

  <div class="abs warranty"><span class="num">50</span><span class="yrs">YEARS</span><span class="roof">ROOF</span><span class="note">WARRANTY</span></div>

  <div class="abs center brand" style="top:436px;font-size:34px"><span class="brand-mark"></span>Quillby</div>
  <div class="abs center brand" style="top:476px;font-size:34px">Housecrafters</div>
  <div class="abs center tagline" style="top:522px">Built Right, Built Local</div>

  <div class="abs center headline teal" style="top:578px;font-size:30px">We are working in</div>
  <div class="abs center headline" style="top:610px;font-size:27px">Your neighborhood</div>
  <div class="abs center headline teal" style="top:648px;font-size:44px">You can</div>
  <div class="abs center headline" style="top:692px;font-size:44px">Find us here</div>

  <div class="abs center phone" style="top:816px">503-555-0148</div>

  <div class="abs center touch" style="top:872px">GET IN<br>TOUCH<br><span class="sub">WITH US</span></div>

  <ul class="abs contact">
    <li><svg width="13" height="13" viewBox="0 0 14 14"><circle cx="7" cy="7" r="6.2" fill="none" stroke="#fff" stroke-width="1.2"/><path d="M3.8 7.2 7 4.4 10.2 7.2V10H3.8Z" fill="#fff"/></svg>Portland, OR 97299, US</li>
    <li><svg width="13" height="13" viewBox="0 0 14 14"><circle cx="7" cy="7" r="6.2" fill="none" stroke="#fff" stroke-width="1.2"/><path d="M4.5 4c.6-.6 1.2-.4 1.6.4l.4.8c.2.4 0 .8-.3 1 .3.8.8 1.3 1.6 1.6.2-.3.6-.5 1-.3l.8.4c.8.4 1 1 .4 1.6C7.6 11 3 6.4 4.5 4Z" fill="#fff"/></svg><strong>(503) 555-0148</strong></li>
    <li><svg width="13" height="13" viewBox="0 0 14 14"><circle cx="7" cy="7" r="6.2" fill="none" stroke="#fff" stroke-width="1.2"/><rect x="3.8" y="4.8" width="6.4" height="4.6" fill="none" stroke="#fff" stroke-width="1"/><path d="M3.8 4.8 7 7.4 10.2 4.8" fill="none" stroke="#fff" stroke-width="1"/></svg>hello@quillbyhousecrafters.com</li>
    <li><svg width="13" height="13" viewBox="0 0 14 14"><circle cx="7" cy="7" r="6.2" fill="none" stroke="#fff" stroke-width="1.2"/><circle cx="7" cy="7" r="3.2" fill="none" stroke="#fff" stroke-width="1"/><path d="M3.8 7H10.2M7 3.8V10.2" stroke="#fff" stroke-width="1"/></svg><span><strong>QuillbyHousecrafters</strong>.com</span></li>
  </ul>

  <div class="abs social">FOLLOW US
    <div class="dots"><span></span><span></span><span></span><span></span><span></span><span></span></div>
    <div class="license">OR #318462<br>WA #QUILLHC7741</div>
  </div>
</section>

<section class="hanger hanger--back">
  <svg class="shapes" width="430" height="1044" viewBox="0 0 430 1044">
    <defs>
      <linearGradient id="washPhoto" x1="0" y1="0" x2="1" y2="1">
        <stop offset="0" stop-color="#5f7a43"/>
        <stop offset="0.5" stop-color="#a9b3a6"/>
        <stop offset="1" stop-color="#3a3d3c"/>
      </linearGradient>
      <linearGradient id="tileRoof" x1="0" y1="0" x2="0" y2="1"><stop offset="0" stop-color="#8fbcd1"/><stop offset="1" stop-color="#4f5c66"/></linearGradient>
      <linearGradient id="tileGutter" x1="0" y1="0" x2="0" y2="1"><stop offset="0" stop-color="#d9d9d6"/><stop offset="1" stop-color="#6a6c70"/></linearGradient>
      <linearGradient id="tilePaint" x1="0" y1="0" x2="0" y2="1"><stop offset="0" stop-color="#c8c9c8"/><stop offset="1" stop-color="#2f3137"/></linearGradient>
      <linearGradient id="tileMasonry" x1="0" y1="0" x2="0" y2="1"><stop offset="0" stop-color="#6b5a46"/><stop offset="1" stop-color="#a8a9a2"/></linearGradient>
      <linearGradient id="tileWash" x1="0" y1="0" x2="1" y2="1"><stop offset="0" stop-color="#b1aca3"/><stop offset="1" stop-color="#7b776f"/></linearGradient>
      <linearGradient id="tileAttic" x1="0" y1="0" x2="0" y2="1"><stop offset="0" stop-color="#8a7b73"/><stop offset="1" stop-color="#4b4240"/></linearGradient>
    </defs>
    <rect width="430" height="360" fill="url(#washPhoto)" role="img" aria-label="Photo of a harnessed worker pressure washing a metal roof among trees"/>
    <polygon points="0,330 214,262 430,330 430,1044 0,1044" fill="var(--teal)"/>
    <polygon points="0,352 214,286 430,352 430,1044 0,1044" fill="var(--charcoal)"/>
    <polygon points="214,222 258,247 258,297 214,322 170,297 170,247" fill="var(--grey)" stroke="var(--charcoal)" stroke-width="3"/>
    <rect x="190" y="361" width="50" height="3" fill="var(--white)"/>

    <rect x="38" y="370" width="174" height="90" rx="10" fill="url(#tileRoof)" role="img" aria-label="Photo of a house roof under construction"/>
    <rect x="218" y="370" width="174" height="90" rx="10" fill="url(#tileGutter)" role="img" aria-label="Photo of a worker cleaning a gutter"/>
    <rect x="38" y="467" width="174" height="88" rx="10" fill="url(#tilePaint)" role="img" aria-label="Photo of a painter spraying siding"/>
    <rect x="218" y="467" width="174" height="88" rx="10" fill="url(#tileMasonry)" role="img" aria-label="Photo of an outdoor kitchen with stone masonry"/>
    <rect x="38" y="562" width="174" height="88" rx="10" fill="url(#tileWash)" role="img" aria-label="Photo of a worker pressure washing a driveway"/>
    <rect x="218" y="562" width="174" height="88" rx="10" fill="url(#tileAttic)" role="img" aria-label="Photo of a roof ridge vent being installed"/>

    <rect x="37" y="672" width="356" height="98" rx="16" fill="none" stroke="var(--teal)" stroke-width="1.6"/>

    <circle cx="50" cy="812" r="22" fill="#e9e9e9" stroke="#8a8a8a" stroke-width="2"/>
    <rect x="118" y="798" width="78" height="34" rx="3" fill="#fff"/>
    <rect x="228" y="790" width="28" height="46" rx="2" fill="#fff"/>
    <rect x="270" y="800" width="120" height="26" rx="4" fill="#4b4a4d"/>
    <rect x="38" y="846" width="72" height="26" fill="#d52a2a"/>
    <circle cx="134" cy="858" r="13" fill="#c9c9cb"/>
    <rect x="154" y="850" width="118" height="16" rx="3" fill="#4b4a4d"/>
    <circle cx="296" cy="858" r="11" fill="#3aa55a"/>
    <rect x="312" y="851" width="82" height="14" rx="3" fill="#4b4a4d"/>

    <polygon points="0,944 215,906 430,944 430,1044 0,1044" fill="var(--grey)"/>
    <polygon points="0,954 215,918 430,954 430,1044 0,1044" fill="var(--teal)"/>
    <rect x="53" y="886" width="325" height="132" rx="14" fill="var(--white)"/>
    <path d="M53,922 V900 A14,14 0 0 1 67,886 H364 A14,14 0 0 1 378,900 V922 Z" fill="var(--teal)"/>

    <circle cx="74" cy="118" r="54" fill="none" stroke="var(--teal-bright)" stroke-width="5"/>
    <circle cx="74" cy="118" r="42" fill="none" stroke="var(--teal-bright)" stroke-width="2"/>
    <polygon points="268,0 430,0 430,150" fill="var(--teal)"/>
    <polygon points="118,0 154,0 236,100 204,120" fill="var(--white)"/>
    <circle cx="226" cy="130" r="80" fill="var(--white)"/>
  </svg>

  <div class="abs corner-flag corner-flag--split" style="left:292px;top:42px"><span class="big">12</span><span class="stack">MONTH<br>INTEREST<br>FREE</span></div>

  <div class="abs brand" style="left:170px;top:262px;width:88px;text-align:center;font-size:10px;color:var(--white);line-height:1.2">Quillby<br>Housecrafters</div>

  <div class="abs center section-title" style="top:332px">OUR SERVICES</div>

  <span class="abs tile-label" style="left:38px;top:443px">Roofing</span>
  <span class="abs tile-label" style="left:218px;top:443px">Gutters</span>
  <span class="abs tile-label" style="left:38px;top:538px">Painting</span>
  <span class="abs tile-label" style="left:218px;top:538px">Masonry &amp; Remodeling</span>
  <span class="abs tile-label" style="left:38px;top:633px">Pressure Washing</span>
  <span class="abs tile-label" style="left:218px;top:633px">Attic Ventilation</span>

  <span class="abs quote-mark" style="left:50px;top:656px;background:var(--charcoal);padding:0 4px">“</span>
  <p class="abs quote">These guys are great. Patient. Answered all our<br>questions and when we ran into a huge problem<br>caused by the previous roofer they were willing<br>to work with us to keep costs down. Highly<br>recommend them. Oh, and the roof is gorgeous!!!</p>
  <div class="abs center quote-name"><span>Dana Whitcombe</span></div>
  <span class="abs quote-mark" style="left:346px;top:758px;background:var(--charcoal);padding:0 4px;height:26px;overflow:hidden">”</span>

  <div class="abs notice-head">WE NOTICE YOU MIGHT NEED<br>SOME WORK DONE</div>
  <ul class="abs notice-list">
    <li>Roof cleaning<span class="lead"></span>$<span class="price"></span></li>
    <li>Moss treatment<span class="lead"></span>$<span class="price"></span></li>
    <li>Gutter cleaning<span class="lead"></span>$<span class="price"></span></li>
    <li>Pressure wash drive-way<span class="lead"></span>$<span class="price"></span></li>
  </ul>
</section>

</body>
</html>
```